Rebrand our dated accomodation business website "Tallowind Quay Residences"

we have a wordpress website ( www.tallowindquay.com.au) that is old and out dated .
I will need a new updated SQUARESPACE website (in which i already have ) with a fresh new design , also new logo and an easy site to manage from my end.
Need to connect our socials - facebook and instagram and our new site
Check out "brindle cove landing" for inspiration...
These apartments are consists of -
-One bedroom One bath
-Two bedroom One bath
-Two bedroom Two bath
-Three bedroom Two bath
all other information is on our current website
KEEP it simple and fresh
ALSO WE DONT HAVE HUGE BIG BOATS IN THE MARINA SO PLEASE DONT HAVE THAT IN THE LOGO

Target Market(s)

Anyone looking for accomodation !! we have 64 rooms !!

Industry/Entity Type

accomodation / short stays

Coding

Coded - Design and coding required

Number of Pages Required

5+ page

Requirements
Must have
• Fresh , modern and easy to use.....have a hoilday vibe , also use natural colours
Nice to have
• i like accomodation website like ....https://fernandgrove.com.au/luxury-coastal-accommodation/ or https://theorvellainn.com/
Should not have
• please do not use bright colours and scripted fonts

```html
<!DOCTYPE html>
<html lang="en">
<head>
<meta charset="utf-8">
<title>Tallowind Quay Residences</title>
<link href="https://fonts.googleapis.com/css2?family=Cormorant+Garamond:wght@500&family=Jost:wght@400;500&display=swap" rel="stylesheet">
<style>
:root{
  --olive:#7a8262;
  --cream:#f6f3ee;
  --card:#f8f6f2;
  --ink:#262626;
  --muted:#6b6b66;
  --brand:#2f6e86;
  --line:#ddd8cf;
}
*{margin:0;padding:0;box-sizing:border-box}
html,body{width:1200px;height:2725px;overflow:hidden}
body{position:relative;background:#fff;color:var(--ink);font-family:'Jost',sans-serif}
.abs{position:absolute}
.serif{font-family:'Cormorant Garamond',serif;font-weight:500;text-transform:uppercase}
.label{font-size:13px;letter-spacing:2px;text-transform:uppercase;color:var(--muted)}
.btn{position:absolute;background:var(--olive);color:#fff;font-size:13px;letter-spacing:1.5px;text-transform:uppercase;display:flex;align-items:center;justify-content:center}
.photo{position:absolute}

.hero{position:absolute;left:0;top:0;width:1200px;height:765px;background:linear-gradient(100deg,#f7efe3 0%,#efe2cc 35%,#c9cfd3 60%,#a79a80 85%,#8a7d63 100%)}
.logo{left:23px;top:52px;font-family:'Cormorant Garamond',serif;font-weight:500;font-size:25px;color:var(--brand);letter-spacing:.5px}
.nav{left:376px;top:64px;display:flex;gap:30px;font-size:12.5px;letter-spacing:1px;text-transform:uppercase}
.nav span.active{border-bottom:1.5px solid var(--ink);padding-bottom:8px}

.features{position:absolute;left:0;top:765px;width:1200px;height:157px;background:var(--cream)}
.feat{position:absolute;top:28px;width:220px;text-align:center;font-size:13.5px;letter-spacing:1px;line-height:23px;text-transform:uppercase}
.feat svg{display:block;margin:0 auto 14px}
.divider{position:absolute;top:38px;width:1px;height:80px;background:var(--line)}

.card{position:absolute;top:1076px;width:248px;height:434px;background:var(--card);border-radius:3px;overflow:hidden}
.card .photo{left:0;top:0;width:248px;height:298px}
.card .info{position:absolute;left:76px;top:324px;font-size:16px;line-height:27px}
.card svg{position:absolute;left:20px;top:330px}
.card .more{position:absolute;left:77px;top:397px;font-size:11.5px;letter-spacing:1.3px;text-transform:uppercase}

.welcome{position:absolute;left:0;top:1597px;width:1200px;height:419px;background:var(--cream)}
.welcome .body{left:668px;top:184px;width:360px;font-size:13.5px;line-height:23.3px;color:#333}

.social-dot{position:absolute;border-radius:50%}

.footer{position:absolute;left:0;top:2466px;width:1200px;height:259px;background:var(--olive);color:#fff}
.footer .label{color:#fff}
.footer .small{font-size:13px;line-height:23px}
.input{position:absolute;left:71px;top:128px;width:221px;height:44px;background:#fff;color:#999;font-size:12.5px;padding:14px 15px}
.subscribe{position:absolute;left:296px;top:128px;width:120px;height:44px;background:#f1eee8;color:var(--ink);font-size:12px;letter-spacing:1px;display:flex;align-items:center;justify-content:center}
.contact{position:absolute;left:838px;font-size:13px;line-height:22px}
.contact svg{position:absolute;left:0;top:3px}
.contact span{display:block;padding-left:34px}
.bar-line{position:absolute;left:0;top:198px;width:1200px;height:1px;background:rgba(255,255,255,.35)}
.bottom{position:absolute;top:218px;font-size:11.5px}
</style>
</head>
<body>

<header class="hero" role="img" aria-label="Sunlit balcony with rattan chairs and palm overlooking a calm marina at sunset"></header>
<div class="abs logo">Tallowind Quay Residences</div>
<nav class="abs nav">
  <span class="active">Home</span><span>About</span><span>Apartments</span><span>Facilities</span><span>Things to do</span><span>Gallery</span><span>Contact</span>
</nav>
<div class="btn" style="left:1030px;top:48px;width:137px;height:48px">Book now</div>
<h1 class="abs serif" style="left:58px;top:252px;font-size:70px;line-height:78px">Waterfront<br>Living, Cove Style</h1>
<p class="abs" style="left:58px;top:428px;font-size:19px;line-height:35px;color:#333">Relax, unwind and enjoy the best of the<br>Brindle Coast at Tallowind Quay Residences.</p>
<div class="btn" style="left:58px;top:532px;width:185px;height:50px">Book your stay</div>

<section class="features">
  <div class="feat" style="left:113px">
    <svg width="54" height="46" viewBox="0 0 54 46" fill="none" stroke="#444" stroke-width="1.3"><path d="M27 4 L18 26 H36 Z"/><path d="M3 32c6-5 10-5 16 0s10 5 16 0 10-5 16 0"/><path d="M3 39c6-5 10-5 16 0s10 5 16 0 10-5 16 0"/></svg>
    Waterfront<br>location</div>
  <div class="divider" style="left:341px"></div>
  <div class="feat" style="left:363px">
    <svg width="54" height="46" viewBox="0 0 54 46" fill="none" stroke="#444" stroke-width="1.3"><circle cx="27" cy="23" r="9"/><path d="M27 4v6M27 36v6M8 23h6M40 23h6M14 10l4 4M36 32l4 4M40 10l-4 4M14 36l4-4"/></svg>
    Resort style<br>facilities</div>
  <div class="divider" style="left:600px"></div>
  <div class="feat" style="left:613px">
    <svg width="54" height="46" viewBox="0 0 54 46" fill="none" stroke="#444" stroke-width="1.3"><path d="M8 20c4-14 34-14 38 0Z"/><path d="M27 20v20"/><path d="M6 40h42"/></svg>
    Close to beach,<br>cafes &amp; shops</div>
  <div class="divider" style="left:850px"></div>
  <div class="feat" style="left:857px">
    <svg width="54" height="46" viewBox="0 0 54 46" fill="none" stroke="#444" stroke-width="1.3"><path d="M27 44c-10-13-14-20-14-27a14 14 0 0 1 28 0c0 7-4 14-14 27Z"/><circle cx="27" cy="17" r="5"/></svg>
    The best of<br>Brindle Cove</div>
</section>

<div class="abs label" style="left:0;width:1200px;text-align:center;top:973px">Our apartments</div>
<h2 class="abs serif" style="left:0;width:1200px;text-align:center;top:996px;font-size:48px">Stay your way</h2>

<div class="card" style="left:61px">
  <div class="photo" role="img" aria-label="Bright bedroom with two beds and neutral linen" style="background:linear-gradient(160deg,#ece4d8,#d2c2a8)"></div>
  <svg width="36" height="38" viewBox="0 0 36 38" fill="none" stroke="#555" stroke-width="1.3"><circle cx="18" cy="11" r="8"/><path d="M3 37c0-9 7-14 15-14s15 5 15 14Z"/></svg>
  <div class="info">One Bedroom<br>One Bath</div><div class="more">View details &rarr;</div>
</div>
<div class="card" style="left:333px">
  <div class="photo" role="img" aria-label="Open living room with sofas and glass doors to marina view" style="background:linear-gradient(180deg,#bcd0dc,#e6ddd0 55%,#cfc1aa)"></div>
  <svg width="44" height="30" viewBox="0 0 44 30" fill="none" stroke="#555" stroke-width="1.3"><circle cx="12" cy="8" r="6"/><circle cx="32" cy="8" r="6"/><path d="M1 29c0-7 5-11 11-11s11 4 11 11ZM21 29c0-7 5-11 11-11s11 4 11 11Z"/></svg>
  <div class="info">Two Bedroom<br>One Bath</div><div class="more">View details &rarr;</div>
</div>
<div class="card" style="left:604px">
  <div class="photo" role="img" aria-label="Living area with armchairs and harbour view windows" style="background:linear-gradient(180deg,#b9ccd6,#e4dace 55%,#cbbb9f)"></div>
  <svg width="44" height="30" viewBox="0 0 44 30" fill="none" stroke="#555" stroke-width="1.3"><circle cx="12" cy="8" r="6"/><circle cx="32" cy="8" r="6"/><path d="M1 29c0-7 5-11 11-11s11 4 11 11ZM21 29c0-7 5-11 11-11s11 4 11 11Z"/></svg>
  <div class="info">Two Bedroom<br>Two Bath</div><div class="more">View details &rarr;</div>
</div>
<div class="card" style="left:876px">
  <div class="photo" role="img" aria-label="Dining and lounge room with table set by balcony windows" style="background:linear-gradient(180deg,#c3d3da,#e6ddd0 55%,#c9b898)"></div>
  <svg width="50" height="30" viewBox="0 0 50 30" fill="none" stroke="#555" stroke-width="1.3"><circle cx="9" cy="8" r="5"/><circle cx="25" cy="8" r="5"/><circle cx="41" cy="8" r="5"/><path d="M1 29c0-6 3-10 8-10s8 4 8 10ZM17 29c0-6 3-10 8-10s8 4 8 10ZM33 29c0-6 3-10 8-10s8 4 8 10Z"/></svg>
  <div class="info">Three Bedroom<br>Two Bath</div><div class="more">View details &rarr;</div>
</div>
<div class="btn" style="left:468px;top:1528px;width:248px;height:48px">View all apartments</div>

<section class="welcome">
  <div class="photo" role="img" aria-label="Aerial view of marina, palms and resort pool with umbrellas" style="left:0;top:6px;width:583px;height:400px;background:linear-gradient(180deg,#a9c4d8 0%,#4f6d52 25%,#6d8fa4 45%,#5f8c57 75%,#3aa3c4 100%)"></div>
  <div class="abs label" style="left:668px;top:56px">Welcome to</div>
  <h2 class="abs serif" style="left:668px;top:80px;font-size:38px;line-height:43px">Tallowind Quay<br>Residences</h2>
  <p class="abs body">Perfectly positioned on the stunning Brindle Cove marina, our self-contained apartments offer the perfect blend of relaxation, comfort and convenience. Whether you're here for a romantic getaway, family holiday or business stay &ndash; you'll love calling Tallowind Quay home.</p>
  <div class="btn" style="left:668px;top:344px;width:121px;height:44px;font-size:12px">About us</div>
</section>

<div class="abs label" style="left:0;width:1200px;text-align:center;top:2042px">Life at the marina</div>
<h2 class="abs serif" style="left:0;width:1200px;text-align:center;top:2068px;font-size:31px">Follow us @tallowindquay</h2>
<div class="photo" role="img" aria-label="Paddleboarder on the water at sunrise" style="left:56px;top:2123px;width:263px;height:252px;background:linear-gradient(180deg,#e8c79a,#b88c5a 50%,#5a4736)"></div>
<div class="photo" role="img" aria-label="Couple dining on a terrace by moored boats" style="left:330px;top:2123px;width:263px;height:252px;background:linear-gradient(180deg,#dfe3e6,#b9b3a6 60%,#6f6557)"></div>
<div class="photo" role="img" aria-label="Palm trees along a waterfront path" style="left:603px;top:2123px;width:263px;height:252px;background:linear-gradient(180deg,#8fb7d8,#c4d8e6 45%,#4d6b46)"></div>
<div class="photo" role="img" aria-label="Guest on a balcony looking over the marina" style="left:877px;top:2123px;width:263px;height:252px;background:linear-gradient(180deg,#b7cbd8,#d8d8d2 50%,#8a8f86)"></div>
<div class="social-dot" aria-label="Social profile link" style="left:548px;top:2399px;width:40px;height:40px;background:var(--ink)"></div>
<div class="social-dot" aria-label="Social profile link" style="left:611px;top:2399px;width:40px;height:40px;border:3px solid var(--ink)"></div>

<footer class="footer">
  <div class="abs label" style="left:71px;top:39px">Stay in the loop</div>
  <div class="abs small" style="left:71px;top:63px">Sign up to receive special offers<br>and local inspiration.</div>
  <div class="input">Your email address</div>
  <div class="subscribe">SUBSCRIBE</div>

  <div class="abs" style="left:400px;width:400px;text-align:center;top:82px;font-family:'Cormorant Garamond',serif;font-weight:500;font-size:27px">Tallowind Quay Residences</div>

  <div class="abs label" style="left:838px;top:39px">Contact us</div>
  <div class="contact" style="top:68px">
    <svg width="16" height="16" viewBox="0 0 16 16" fill="#fff"><path d="M3 1h3l1.5 4-2 1.3a9 9 0 0 0 4.2 4.2L11 8.5 15 10v3a2 2 0 0 1-2 2A12 12 0 0 1 1 3a2 2 0 0 1 2-2Z"/></svg>
    <span>02 5550 3184</span></div>
  <div class="contact" style="top:102px">
    <svg width="16" height="14" viewBox="0 0 16 14" fill="#fff"><path d="M0 1h16v12H0Z"/><path d="M0 1l8 6 8-6" stroke="#7a8262" stroke-width="1.5" fill="none"/></svg>
    <span>stay@tallowindquay.com.au</span></div>
  <div class="contact" style="top:137px">
    <svg width="14" height="18" viewBox="0 0 14 18" fill="#fff"><path d="M7 18C2 11 0 8 0 6.5a7 7 0 0 1 14 0C14 8 12 11 7 18Z"/><circle cx="7" cy="6.5" r="2.4" fill="#7a8262"/></svg>
    <span>14 Quayside Parade, Brindle Cove<br>NSW 2999</span></div>

  <div class="bar-line"></div>
  <div class="bottom" style="left:71px">&copy; 2025 Tallowind Quay Residences. All Rights Reserved.</div>
  <div class="bottom" style="left:555px">Privacy Policy &nbsp;&nbsp;&nbsp;|&nbsp;&nbsp;&nbsp; Terms &amp; Conditions</div>
  <div class="social-dot" aria-label="Social profile link" style="left:1051px;top:218px;width:20px;height:20px;background:#fff"></div>
  <div class="social-dot" aria-label="Social profile link" style="left:1090px;top:218px;width:20px;height:20px;border:2px solid #fff"></div>
</footer>

</body>
</html>
```